CALM.OTTER snowsport and living

Calm Otter webpage design brief

Calm Otter is a life style brand
for those who love winter, snowboarding, and coffee.

We have log houses at some best snowboarding locations in Japan, in which easy and comfortable ambience make guests feel at home during their winter stay. Out there on the slopes, there are Calm Otter’s exclusive coffee kiosks that offer a wide selection of fine coffee from boutique roasters over the world to warm the hands and hearts of whenever our guests need!

Enjoy the snow with Calm Otter!

Tone & Manner: Simple, Tranquil, Relaxed, Enjoyable
 
Look and Feel : Monotone images of log house in the snowy winter and snowboarding people.  Capture of real-people-real-life moments. Red and blue colors can be used on icons and other vector elements in a much smaller scale in the overall picture.  Please refer to the attached color pallette.

Mainly informational with links to Stayvorn for booking
Social media registration pass over from talkloop. pagemural or Stayvorn
Recruitment link to Jobvane

Currently I do not have any pictures. So need a bit of discussion on this area.

Also the website needs to be in 3 languages, English, Chinese and Japanese.

Rough Sitemap:

Home (language selection on every page)
About
GO (snow villas)
Coffee (coffee kiosks on slopes)
Reservations

(Bottom of screen)
Contact us
Company info
Recruit

Reference website:
Quillbrook.example
Mossgate.example.jp

Attached pictures are for references not for use!!!
Color reference pls refer to attached file 4.

Reason: More updates on project briefs. Please have a look.

Target Market(s)

Snowboarders

Industry/Entity Type

Hospitality

Number of Pages Required

5+ page

Font styles to use
Sans Serif

Colors

Designer to choose colors to be used in the design.

Requirements
Must have
• Mobile version
• 3 languages
• Registration thru TalkLoop, Pagemural or Stayvorn
Nice to have
• Illustration instead of pictures

```html
<!DOCTYPE html>
<html lang="en">
<head>
<meta charset="utf-8">
<title>Calm Otter — Snowsport and Living</title>
<link rel="stylesheet" href="https://fonts.googleapis.com/css2?family=Oswald:wght@300;400&display=swap">
<style>
  :root {
    --red: #c9232f;
    --navy: #2b2f40;
    --ink: #2e3140;
    --muted: #4a4d5a;
    --white: #ffffff;
    --line: #d9d9de;
    --sketch: #eceef3;
  }
  * { box-sizing: border-box; margin: 0; padding: 0; }
  html, body { width: 1200px; height: 3136px; overflow: hidden; background: var(--white); }
  body { font-family: "Oswald", "Arial Narrow", sans-serif; font-weight: 300; color: var(--ink); }

  .site-header {
    height: 78px; border-bottom: 1px solid var(--line);
    display: flex; align-items: center; padding: 0 100px; position: relative;
  }
  .brand { color: var(--red); font-size: 17px; font-weight: 300; letter-spacing: 1.5px; }
  .main-nav { position: absolute; left: 320px; display: flex; gap: 33px; }
  .main-nav a { color: var(--ink); text-decoration: none; font-size: 14px; letter-spacing: 1.2px; }
  .lang-select {
    position: absolute; left: 955px; top: 21px; width: 145px; height: 36px;
    border: 1px solid var(--muted); border-radius: 2px;
    display: flex; align-items: center; justify-content: center; gap: 18px;
    font-size: 13px; letter-spacing: 1.2px;
  }

  .intro { height: 512px; position: relative; text-align: center; }
  .intro-title { position: absolute; top: 208px; width: 100%; color: var(--red); font-weight: 400; font-size: 33px; letter-spacing: 2px; }
  .intro-sub { position: absolute; top: 274px; width: 100%; font-size: 13px; letter-spacing: 1.5px; }
  .intro-art { position: absolute; top: 268px; width: 390px; height: 200px; border-radius: 4px;
    background: linear-gradient(180deg, var(--white), var(--sketch)); }
  .intro-art.left { left: 100px; }
  .intro-art.right { left: 710px; }
  .scroll-arrow { position: absolute; left: 584px; top: 345px; }

  .feature-grid { display: grid; grid-template-columns: 600px 600px; grid-auto-rows: 510px; }
  .feature-text { background: var(--navy); color: var(--white); text-align: center; padding-top: 138px; }
  .feature-text h2 { color: var(--red); font-weight: 400; font-size: 31px; letter-spacing: 2.5px; }
  .feature-text p { width: 410px; margin: 34px auto 0; font-size: 14px; line-height: 27px; letter-spacing: 1.4px; text-transform: uppercase; }
  .more-link { display: inline-flex; align-items: center; gap: 12px; margin-top: 50px;
    color: var(--white); text-decoration: none; font-size: 20px; letter-spacing: 2px; font-weight: 400; }
  .photo { width: 100%; height: 100%; }
  .photo-village { background: linear-gradient(180deg, #5f7bb8 0%, #7b8fbf 40%, #3a3f5c 70%, #c3c9dc 100%); }
  .photo-cafe { background: radial-gradient(circle at 30% 40%, #d98a2c 0%, #8a3a14 45%, #2a120a 100%); }
  .photo-team { background: linear-gradient(180deg, #8e9692 0%, #e9ecef 35%, #2b2b2e 55%, #3b3d44 80%, #eef0f2 100%); }
  .photo-lodge { background: linear-gradient(180deg, #0e2a8a 0%, #1f3fb0 40%, #c9a25a 60%, #2a48c2 80%, #6d86e0 100%); }

  .questions { text-align: center; position: relative; height: 508px; }
  .questions h2 { position: absolute; top: 158px; width: 100%; color: var(--red); font-weight: 400; font-size: 33px; letter-spacing: 2px; }
  .questions p { position: absolute; top: 227px; width: 100%; font-size: 13px; letter-spacing: 1.5px; }
  .questions .more-link { position: absolute; top: 346px; left: 0; right: 0; justify-content: center; color: var(--ink); margin: 0; }
</style>
</head>
<body>
  <header class="site-header">
    <div class="brand">CALM OTTER</div>
    <nav class="main-nav">
      <a href="#">HOME</a><a href="#">ABOUT</a><a href="#">GO</a><a href="#">COFFEE</a>
      <a href="#">RESERVATIONS</a><a href="#">CONTACT US</a><a href="#">LOG IN</a>
    </nav>
    <div class="lang-select">ENGLISH
      <svg width="12" height="8" viewBox="0 0 12 8"><path d="M1 1l5 5 5-5" fill="none" stroke="#2e3140" stroke-width="1.2"/></svg>
    </div>
  </header>

  <section class="intro">
    <h1 class="intro-title">LOREM IPSUM DOLOR SET AMET</h1>
    <p class="intro-sub">LOREM IPSUM DOLOR</p>
    <div class="intro-art left" role="img" aria-label="Line illustration of snowy mountains, a log house, coffee cups and a snowman"></div>
    <div class="intro-art right" role="img" aria-label="Mirrored line illustration of a snowman, coffee, a log house and mountains"></div>
    <svg class="scroll-arrow" width="32" height="40" viewBox="0 0 32 40"><path d="M16 2v34M4 24l12 12 12-12" fill="none" stroke="#2e3140" stroke-width="1.6"/></svg>
  </section>

  <main class="feature-grid">
    <div class="feature-text">
      <h2>SNOW WILLAS</h2>
      <p>We have log houses at some best snowboarding locations in Japan, in which easy and comfortable ambience make guests feel at home during their winter stay.</p>
      <a class="more-link" href="#">LEARN MORE <svg width="24" height="16" viewBox="0 0 24 16"><path d="M1 8h21M15 1l7 7-7 7" fill="none" stroke="#fff" stroke-width="1.4"/></svg></a>
    </div>
    <div class="photo photo-village" role="img" aria-label="Photo of a snowy alpine village street lit up at dusk"></div>

    <div class="photo photo-cafe" role="img" aria-label="Photo of a warm, busy wood-panelled café interior"></div>
    <div class="feature-text">
      <h2>COFFEE KIOSKS</h2>
      <p>Out there on the slopes, there are Calm Otter’s exclusive coffee kiosks that offer a wide selection of fine coffee from boutique roasters over the world to warm the hands and hearts of whenever our guests need!</p>
      <a class="more-link" href="#">LEARN MORE <svg width="24" height="16" viewBox="0 0 24 16"><path d="M1 8h21M15 1l7 7-7 7" fill="none" stroke="#fff" stroke-width="1.4"/></svg></a>
    </div>

    <div class="feature-text">
      <h2>OUR TEAM</h2>
      <p>Our professional team is a knowledge based group which works hard to make sure you you're taken care of. We just love what we do, and we want you to be a part of our love.</p>
      <a class="more-link" href="#">COMPANY INFO <svg width="24" height="16" viewBox="0 0 24 16"><path d="M1 8h21M15 1l7 7-7 7" fill="none" stroke="#fff" stroke-width="1.4"/></svg></a>
    </div>
    <div class="photo photo-team" role="img" aria-label="Photo of the team standing together in the snow"></div>

    <div class="photo photo-lodge" role="img" aria-label="Photo of a log lodge lit up on a snowy evening"></div>
    <div class="feature-text">
      <h2>HURRY UP</h2>
      <p>Unforgettable holidays. This is what you'll get there.<br>It is a unique opportunity to relax and unwind.<br>Make a reservation today - the number of villas is limited!</p>
      <a class="more-link" href="#">RESERVE <svg width="24" height="16" viewBox="0 0 24 16"><path d="M1 8h21M15 1l7 7-7 7" fill="none" stroke="#fff" stroke-width="1.4"/></svg></a>
    </div>
  </main>

  <section class="questions">
    <h2>STILL HAVE ANY QUESTIONS?</h2>
    <p>WE ARE HAPPY TO HELP YOU!</p>
    <a class="more-link" href="#">CONTACT US <svg width="24" height="16" viewBox="0 0 24 16"><path d="M1 8h21M15 1l7 7-7 7" fill="none" stroke="#2e3140" stroke-width="1.4"/></svg></a>
  </section>
</body>
</html>
```